Small boutique multi-family apartment developer needs premium website design.

We are a growing real estate development company specializing in multi family apartment development. Our company Mireval Stone Development focuses on passive real estate investors looking to maximize their current real estate portfolio by allowing us to develop and reposition their current properties allowing them more cashflow while we are also able to take over the management of their asset in order to ensure optimal performance on a consistent basis.

```html
<!DOCTYPE html>
<html lang="en">
<head>
<meta charset="utf-8">
<title>Mireval Stone Development</title>
<link href="https://fonts.googleapis.com/css2?family=Montserrat:wght@400;500;700;800&family=Open+Sans:wght@300;400&display=swap" rel="stylesheet">
<style>
:root{
  --brand:#6592e8;
  --brand-dark:#3f63c4;
  --brand-light:#a9c4f3;
  --ink:#555b66;
  --white:#ffffff;
  --rule:#e2e2e2;
}
*{box-sizing:border-box;margin:0;padding:0}
html,body{width:1200px;height:2689px;overflow:hidden;background:var(--white)}
body{position:relative;font-family:"Open Sans",sans-serif;color:var(--ink)}
.abs{position:absolute}
.btn{position:absolute;display:flex;align-items:center;justify-content:center;background:var(--brand);color:var(--white);font-family:"Open Sans",sans-serif;font-size:14px;font-weight:400;text-transform:uppercase}

/* header */
.site-header{left:0;top:0;width:1200px;height:92px;background:var(--brand)}
.brand{left:140px;top:22px;color:var(--white);font-family:"Montserrat",sans-serif;font-weight:700;font-size:26px;letter-spacing:1px;line-height:1}
.brand small{display:block;font-size:9px;font-weight:500;letter-spacing:4.4px;margin-top:5px}
.nav{left:650px;top:40px;display:flex;gap:31px;color:var(--white);font-size:13px}
.nav-cta{left:913px;top:30px;width:148px;height:35px;background:var(--white);color:var(--brand);font-size:13px}

/* hero */
.hero{left:0;top:92px;width:1200px;height:540px;background:linear-gradient(180deg,#3fd6f5 0%,#7fd8f4 45%,#d6ecf7 80%,#eaf3f8 100%)}
.hero-photo{left:555px;top:92px;width:645px;height:540px;background:linear-gradient(160deg,#9cd2ee 0%,#5a92c0 35%,#3d6480 65%,#c7cbd0 100%)}
.hero-tree{left:0;top:500px;width:140px;height:132px;background:linear-gradient(180deg,#7ac14a,#3d7b22)}
.hero-kicker{left:87px;top:236px;font-family:"Montserrat",sans-serif;font-size:21px;color:var(--brand-dark);font-weight:400}
.hero-title{left:86px;top:256px;font-family:"Montserrat",sans-serif;font-size:51px;font-weight:800;color:var(--brand-dark);letter-spacing:.5px}
.hero-sub{left:91px;top:320px;width:460px;font-family:"Montserrat",sans-serif;font-size:17px;color:var(--brand-dark);line-height:21px}
.hero-cta{left:88px;top:383px;width:148px;height:42px}

/* team */
.team-photo{left:160px;top:569px;width:584px;height:396px;background:linear-gradient(180deg,#cfd6dc 0%,#8e969d 50%,#3a3d42 100%)}
.team-card{left:593px;top:821px;width:469px;height:238px;background:var(--white);box-shadow:0 0 14px rgba(0,0,0,.12)}
.team-card h2{position:absolute;left:30px;top:22px;font-family:"Montserrat",sans-serif;font-weight:700;font-size:28px;color:var(--brand-dark)}
.team-card p{position:absolute;left:33px;top:64px;width:392px;font-size:13px;font-weight:300;line-height:22.5px;text-align:justify}
.team-card .btn{left:30px;top:171px;width:148px;height:39px}
.skyline-art{left:915px;top:673px;width:145px;height:148px;background:linear-gradient(180deg,#e4ecfb,#9dbbf0)}

/* expertise */
.expertise{left:0;top:1129px;width:1200px;height:360px;background:var(--brand);color:var(--white);text-align:center}
.expertise h2{position:absolute;left:0;width:1200px;top:28px;font-family:"Montserrat",sans-serif;font-weight:700;font-size:29px;line-height:34px}
.expertise p.lead{position:absolute;left:280px;width:640px;top:105px;font-size:12.5px;font-weight:300;line-height:23px}
.service{position:absolute;top:193px;width:160px;font-size:14px;font-weight:300;line-height:22px}
.service .ring{width:78px;height:78px;border-radius:50%;background:rgba(255,255,255,.22);margin:0 auto 14px;display:flex;align-items:center;justify-content:center}
.band-art{left:0;top:1265px;width:128px;height:224px;background:linear-gradient(90deg,#8fb1ee,#7aa2ec)}

/* portfolio */
.portfolio-title{left:136px;top:1551px;font-family:"Montserrat",sans-serif;font-weight:700;font-size:29px;color:var(--brand-dark)}
.portfolio-lead{left:138px;top:1593px;width:640px;font-size:12.5px;font-weight:300;line-height:23px;color:#6b717a}
.view-all{left:915px;top:1578px;width:148px;height:42px}
.property{position:absolute;top:1669px;width:302px;height:372px}
.property .shot{width:302px;height:323px}
.property .label{height:48px;background:var(--brand);color:var(--white);font-size:14px;display:flex;align-items:center;padding-left:14px;text-transform:uppercase;white-space:nowrap;overflow:hidden}
.slider-track{left:363px;top:2083px;width:553px;height:7px;background:var(--rule)}
.slider-thumb{left:363px;top:2083px;width:142px;height:7px;background:var(--brand)}

/* cta */
.cta{left:0;top:2165px;width:1200px;height:214px;background:linear-gradient(180deg,#aeb7bf 0%,#8d9399 50%,#6b7076 100%)}
.cta h2{position:absolute;left:0;width:1200px;top:62px;text-align:center;font-family:"Montserrat",sans-serif;font-weight:700;font-size:29px;color:var(--white)}
.cta p{position:absolute;left:0;width:1200px;top:99px;text-align:center;font-size:13px;font-weight:300;color:var(--white)}
.cta .btn{left:506px;top:126px;width:188px;height:42px}

/* footer */
.site-footer{left:0;top:2379px;width:1200px;height:257px;background:var(--brand);color:var(--white)}
.footer-brand{position:absolute;left:0;width:1200px;top:44px;text-align:center;font-family:"Montserrat",sans-serif;font-weight:700;font-size:46px;letter-spacing:2px;line-height:1}
.footer-brand small{display:block;font-size:12px;font-weight:500;letter-spacing:7px;margin-top:8px}
.footer-rule{position:absolute;left:223px;top:130px;width:754px;height:2px;background:rgba(255,255,255,.45)}
.contact{position:absolute;top:160px;display:flex;align-items:center;gap:10px}
.contact .dot{width:58px;height:58px;border-radius:50%;background:rgba(255,255,255,.3);display:flex;align-items:center;justify-content:center}
.contact h3{font-family:"Montserrat",sans-serif;font-weight:700;font-size:14px}
.contact p{font-size:13px;font-weight:300;line-height:22px}
.divider{position:absolute;top:150px;width:2px;height:80px;background:rgba(255,255,255,.45)}
.copyright{left:147px;top:2655px;font-family:"Montserrat",sans-serif;font-size:12px;color:#666}
.social{left:965px;top:2652px;display:flex;gap:16px}
.social span{width:17px;height:17px;border-radius:50%;background:var(--brand)}
</style>
</head>
<body>

<header class="abs site-header">
  <div class="abs brand">MIREVAL STONE<small>DEVELOPMENT</small></div>
  <nav class="abs nav"><span>ABOUT</span><span>SERVICES</span><span>PROPERTIES</span></nav>
  <div class="btn nav-cta">CONTACT US</div>
</header>

<section class="abs hero"></section>
<div class="abs hero-photo" role="img" aria-label="Modern apartment and glass office towers against a blue sky"></div>
<div class="abs hero-tree" role="img" aria-label="Green tree canopy"></div>
<div class="abs hero-kicker">TRANSFORMING PROPERTIES</div>
<h1 class="abs hero-title">MAXIMIZING RETURNS</h1>
<p class="abs hero-sub">Partner with Mireval Stone Development to optimize your real estate portfolio</p>
<div class="btn hero-cta">CONTACT US</div>

<div class="abs team-photo" role="img" aria-label="Four team members in business attire standing by office windows"></div>
<div class="abs skyline-art" role="img" aria-label="Decorative illustration of building bars with sun and clouds"></div>
<div class="abs team-card">
  <h2>MEET OUR TEAM</h2>
  <p>Our experienced team is dedicated to helping passive real estate investors maximize their portfolio's potential. With a focus on multi-family apartment development, we're committed to delivering exceptional results</p>
  <div class="btn">GET STARTED</div>
</div>

<section class="abs expertise">
  <h2>OUR EXPERTISE IN MULTI-FAMILY APARTMENT<br>DEVELOPMENT</h2>
  <p class="lead">We specialize in developing and repositioning properties to increase cash flow and optimize performance. Our services are designed to help you achieve your real estate goals</p>
  <div class="service" style="left:210px"><div class="ring"><svg width="40" height="40" viewBox="0 0 40 40" fill="none" stroke="#fff" stroke-width="2"><rect x="12" y="6" width="16" height="16"/><circle cx="20" cy="28" r="6"/><path d="M4 34h32"/></svg></div>Passive Real Estate<br>Investing</div>
  <div class="service" style="left:425px"><div class="ring"><svg width="40" height="40" viewBox="0 0 40 40" fill="none" stroke="#fff" stroke-width="2"><path d="M6 20L20 8l14 12"/><path d="M11 17v15h18V17"/><rect x="17" y="24" width="6" height="8"/></svg></div>Property<br>Development</div>
  <div class="service" style="left:640px"><div class="ring"><svg width="40" height="40" viewBox="0 0 40 40" fill="none" stroke="#fff" stroke-width="2"><rect x="9" y="6" width="22" height="28"/><path d="M13 13h14M13 19h14M13 25h10"/></svg></div>Property<br>Management</div>
  <div class="service" style="left:852px"><div class="ring"><svg width="40" height="40" viewBox="0 0 40 40" fill="none" stroke="#fff" stroke-width="2"><circle cx="20" cy="20" r="12"/><path d="M20 13v14M16 17h7M17 23h7"/></svg></div>Asset<br>Optimization</div>
</section>
<div class="abs band-art" role="img" aria-label="Decorative building silhouettes"></div>

<h2 class="abs portfolio-title">OUR PORTFOLIO</h2>
<p class="abs portfolio-lead">We specialize in developing and repositioning properties to increase cash flow and optimize performance. Our services are designed to help you achieve your real estate goals</p>
<div class="btn view-all">VIEW ALL</div>

<div class="property" style="left:138px"><div class="shot" role="img" aria-label="Modern dark-framed apartment building" style="background:linear-gradient(160deg,#c9dcef,#6f8aa8 60%,#2d3642)"></div><div class="label">VISTA HEIGHTS RESIDENCES</div></div>
<div class="property" style="left:458px"><div class="shot" role="img" aria-label="Tall apartment tower with balconies" style="background:linear-gradient(170deg,#9cb8cf,#7a6f62 60%,#4a423a)"></div><div class="label">HARBORVIEW LOFTS</div></div>
<div class="property" style="left:780px"><div class="shot" role="img" aria-label="Orange brick high-rise beside a glass tower" style="background:linear-gradient(160deg,#3a7fe0,#c4643a 55%,#2c3e66)"></div><div class="label">WILLOWBROOK ESTATES</div></div>
<div class="property" style="left:1101px"><div class="shot" role="img" aria-label="City skyline at sunset" style="background:linear-gradient(180deg,#f0b54a,#e08a2a 70%,#5a4a3a)"></div><div class="label">SUNSET GROVE</div></div>

<div class="abs slider-track"></div>
<div class="abs slider-thumb"></div>

<section class="abs cta" role="img" aria-label="Aerial view of a city skyline">
  <h2>READY TO TRANSFORM YOUR PORTFOLIO?</h2>
  <p>Contact us to learn more about our services and how we can help you maximize your real estate portfolio</p>
  <div class="btn">GET STARTED TODAY</div>
</section>

<footer class="abs site-footer">
  <div class="footer-brand">MIREVAL STONE<small>DEVELOPMENT</small></div>
  <div class="footer-rule"></div>
  <div class="contact" style="left:208px">
    <div class="dot"><svg width="26" height="26" viewBox="0 0 24 24" fill="#fff"><path d="M6.6 10.8a15 15 0 006.6 6.6l2.2-2.2a1 1 0 011-.25 11.4 11.4 0 003.6.57 1 1 0 011 1V20a1 1 0 01-1 1A17 17 0 013 4a1 1 0 011-1h3.5a1 1 0 011 1c0 1.25.2 2.45.57 3.57a1 1 0 01-.25 1z"/></svg></div>
    <div><h3>GIVE US A CALL</h3><p>+12 3000 555 010</p></div>
  </div>
  <div class="divider" style="left:430px"></div>
  <div class="contact" style="left:472px">
    <div class="dot"><svg width="30" height="22" viewBox="0 0 30 22" fill="none" stroke="#fff" stroke-width="2"><rect x="1" y="1" width="28" height="20"/><path d="M1 1l14 11L29 1"/></svg></div>
    <div><h3>EMAIL ADDRESS</h3><p>info@mirevalstone.com</p></div>
  </div>
  <div class="divider" style="left:723px"></div>
  <div class="contact" style="left:758px">
    <div class="dot"><svg width="22" height="28" viewBox="0 0 22 28" fill="#fff"><path d="M11 0a11 11 0 00-11 11c0 8 11 17 11 17s11-9 11-17A11 11 0 0011 0zm0 15a4 4 0 110-8 4 4 0 010 8z"/></svg></div>
    <div><h3>ADDRESS</h3><p>Lorem ipsum dolor sit amet,<br>consectetur adipiscing elit</p></div>
  </div>
</footer>

<div class="abs copyright">© 2024 mireval stone development. all rights reserved</div>
<div class="abs social"><span aria-label="Social profile"></span><span aria-label="Social profile"></span><span aria-label="Social profile"></span></div>

</body>
</html>
```